Harmony Swift Care Business card

We want a business card that matches our business theme. Our website is www.swiftcarehub.example
The company name is Harmony Swift Care
The persons having the business cards will be doctors
My logo is attached.
We have a drive-thru medical center where our motto is Fast, Reliable, and Convenient. Our goal is to change the medical space while utilizing technologies, keeping a professional and clean look

Medical

Info on the card should be: Name, Position, Cell number, website, email address, possibly the office line as well

Requirements
Must have
• Logo
Nice to have
• Professional medical feel with our logo colors incorporated

```html
<!DOCTYPE html>
<html lang="en">
<head>
<meta charset="utf-8">
<title>Harmony Swift Care – Business Card</title>
<link href="https://fonts.googleapis.com/css2?family=Lato:wght@400;700;900&display=swap" rel="stylesheet">
<style>
  :root {
    --stage: #2b2b2d;
    --card: #1c1d20;
    --card-back-top: #3a3b3e;
    --card-back-bottom: #0d0d0f;
    --brand-blue: #1f4fb4;
    --brand-sky: #3cc3f2;
    --ink-light: #f2f3f5;
    --rule: #6b6d72;
  }
  * { box-sizing: border-box; margin: 0; padding: 0; }
  html, body {
    width: 1200px; height: 1108px; overflow: hidden;
    background: var(--stage);
    font-family: "Lato", Arial, sans-serif;
  }
  .stage { position: relative; width: 1200px; height: 1108px; }
  .card {
    position: absolute; top: 169px;
    width: 440px; height: 770px;
    border-radius: 26px;
    overflow: hidden;
  }
  .card--front { left: 120px; background: var(--card); }
  .card--back { left: 640px; }

  .brand {
    position: absolute; top: 150px; left: 0; right: 0;
    display: flex; align-items: center; justify-content: center; gap: 22px;
  }
  .brand__name {
    color: var(--brand-blue);
    font-weight: 900; font-size: 44px; line-height: 1.02;
    text-align: right;
  }
  .brand__mark {
    width: 96px; height: 96px; border-radius: 50%;
    border: 12px solid var(--brand-blue);
  }
  .tagline {
    position: absolute; top: 286px; left: 0; right: 0;
    text-align: center; color: var(--ink-light);
    font-size: 17px; letter-spacing: 2px;
  }

  .person { position: absolute; top: 450px; left: 0; right: 0; text-align: center; }
  .person__name { color: var(--brand-blue); font-weight: 700; font-size: 36px; }
  .person__role { color: var(--ink-light); font-size: 26px; margin-top: 2px; }

  .contact-icons {
    position: absolute; top: 555px; left: 40px; right: 40px;
    display: flex; align-items: center; gap: 10px;
  }
  .contact-icons__rule { flex: 1; height: 1px; background: var(--rule); }
  .contact-icons__item {
    width: 34px; height: 34px; border-radius: 5px;
    background: var(--brand-blue);
    display: flex; align-items: center; justify-content: center;
  }
  .contact-icons__item svg { width: 22px; height: 22px; }

  .contact-list {
    position: absolute; top: 610px; left: 0; right: 0;
    list-style: none; text-align: center;
    color: var(--ink-light); font-size: 23px; line-height: 1.35;
  }
  .contact-list__domain { color: var(--brand-sky); }

  .back-pattern {
    position: absolute; inset: 0;
    background: linear-gradient(35deg, var(--card-back-bottom) 30%, var(--card-back-top) 100%);
  }
  .back-mark {
    position: absolute; left: 300px; top: 560px;
    width: 54px; height: 54px; border-radius: 50%;
    border: 8px solid var(--brand-blue);
  }
</style>
</head>
<body>
<main class="stage">

  <section class="card card--front" aria-label="Business card front">
    <div class="brand">
      <div class="brand__name">Harmony<br>Swift Care</div>
      <div class="brand__mark"></div>
    </div>
    <p class="tagline">FAST | RELIABLE | CONVENIENT</p>

    <div class="person">
      <h1 class="person__name">Daniel Marsh</h1>
      <p class="person__role">Managing Director</p>
    </div>

    <div class="contact-icons">
      <span class="contact-icons__rule"></span>
      <span class="contact-icons__item" title="Office">
        <svg viewBox="0 0 24 24" fill="none" stroke="#1c1d20" stroke-width="2"><path d="M4 9c0-3 4-4 8-4s8 1 8 4l-3 1-1-2H8l-1 2z"/><rect x="6" y="12" width="12" height="7" rx="1"/></svg>
      </span>
      <span class="contact-icons__item" title="Mobile">
        <svg viewBox="0 0 24 24" fill="none" stroke="#1c1d20" stroke-width="2"><rect x="7" y="3" width="10" height="18" rx="2"/><line x1="11" y1="18" x2="13" y2="18"/></svg>
      </span>
      <span class="contact-icons__item" title="Email">
        <svg viewBox="0 0 24 24" fill="none" stroke="#1c1d20" stroke-width="2"><rect x="3" y="6" width="18" height="12"/><path d="M3 6l9 7 9-7"/></svg>
      </span>
      <span class="contact-icons__item" title="Website">
        <svg viewBox="0 0 24 24" fill="none" stroke="#1c1d20" stroke-width="2"><circle cx="12" cy="12" r="8"/><path d="M4 12h16M12 4c3 3 3 13 0 16M12 4c-3 3-3 13 0 16"/></svg>
      </span>
      <span class="contact-icons__rule"></span>
    </div>

    <ul class="contact-list">
      <li>055-010 246 802</li>
      <li>055-010 246 802</li>
      <li>info@swiftcarehub.example</li>
      <li>www.<span class="contact-list__domain">swiftcarehub</span>.example</li>
    </ul>
  </section>

  <section class="card card--back" aria-label="Business card back">
    <div class="back-pattern" role="img" aria-label="Repeating embossed pattern of the brand emblem in glossy grey tones"></div>
    <div class="back-mark"></div>
  </section>

</main>
</body>
</html>
```